Financial Services Sales Sheet

We need this sheet redesigned. Needs to feel very corporate/financial. open to imagery/icons/colors/etc. Copy is in the docx file to expedite work. PDF is what client has done inh-house and feels dated.

```html
<!DOCTYPE html>
<html lang="en">
<head>
<meta charset="utf-8">
<title>Harborline Portfolio Partners – Master Servicing &amp; Portfolio Optimization</title>
<link rel="stylesheet" href="https://fonts.googleapis.com/css2?family=Nunito:wght@700;800;900&family=Montserrat:wght@400;500;600;700&display=swap">
<style>
:root{
  --navy:#1b3a6e;
  --navy-deep:#142d58;
  --blue:#1f5aa6;
  --blue-bright:#2a6fc4;
  --ice:#eaf1fa;
  --ink:#1d2433;
  --white:#ffffff;
  --line:#c9d6ea;
}
*{box-sizing:border-box;margin:0;padding:0}
html,body{width:1200px;height:2250px;overflow:hidden;background:var(--white)}
body{font-family:"Montserrat",sans-serif;color:var(--ink);position:relative}
.sheet{position:relative;width:1200px;height:2250px;background:var(--white);overflow:hidden}
.abs{position:absolute}

/* header */
.brand{left:80px;top:50px;display:flex;align-items:center;gap:22px}
.brand-mark{width:64px;height:64px;background:var(--navy);border-radius:6px}
.brand-name{font-family:"Nunito",sans-serif;font-weight:900;color:var(--navy);font-size:34px;line-height:1.02;letter-spacing:.3px}
.brand-tag{font-family:"Nunito",sans-serif;font-weight:800;color:var(--navy);font-size:15px;letter-spacing:.6px;margin-top:6px;text-transform:uppercase}
.hero-photo{left:0;top:0;width:1200px;height:720px}
.hero-panel{left:0;top:0;width:1200px;height:720px}
.hero-copy{left:82px;top:210px;width:580px;color:var(--white)}
.hero-title{font-family:"Nunito",sans-serif;font-weight:900;font-size:49px;line-height:1.1}
.hero-sub{font-family:"Nunito",sans-serif;font-weight:800;font-size:22px;line-height:1.22;margin-top:18px}
.hero-rule{width:140px;height:3px;background:var(--white);margin:22px 0 20px}
.hero-body{font-size:20px;line-height:1.3;font-weight:500}

/* services */
.service-band{left:25px;top:960px;width:1150px;height:470px;background:var(--navy);border-radius:22px}
.services{left:58px;top:760px;width:1084px;height:470px;background:var(--white);border:3px solid var(--navy);border-radius:24px;display:flex;padding:34px 16px 26px}
.service{flex:1;padding:0 14px;border-right:1px solid var(--line)}
.service:last-child{border-right:none}
.service-head{display:flex;gap:12px;align-items:flex-start;padding-bottom:18px;border-bottom:2px solid var(--line);margin-bottom:20px;position:relative}
.service-head::after{content:"";position:absolute;left:0;bottom:-2px;width:52px;height:2px;background:var(--blue)}
.service-icon{width:44px;height:44px;flex:none;background:var(--blue);border-radius:6px;display:flex;align-items:center;justify-content:center}
.service-title{font-family:"Nunito",sans-serif;font-weight:800;font-size:20px;line-height:1.2;color:var(--ink)}
.service ul{list-style:none}
.service li{position:relative;padding-left:18px;font-size:17px;line-height:1.45;font-weight:500}
.service li::before{content:"";position:absolute;left:2px;top:10px;width:6px;height:6px;border-radius:50%;background:var(--ink)}

/* performance */
.snapshot-title{left:0;top:1252px;width:1200px;text-align:center;color:var(--white);font-family:"Montserrat",sans-serif;font-weight:700;font-size:32px;letter-spacing:9px}
.stats{left:88px;top:1312px;width:1024px;display:flex;gap:14px}
.stat{flex:1;min-width:0;height:156px;border:3px solid var(--white);border-radius:16px;background:linear-gradient(180deg,var(--blue) 0%,var(--navy) 100%);color:var(--white);text-align:center;padding-top:24px}
.stat-num{font-family:"Montserrat",sans-serif;font-weight:500;font-size:40px;line-height:1;white-space:nowrap}
.stat-num small{font-size:19px;font-weight:600}
.stat-label{font-size:17px;line-height:1.2;margin-top:14px;opacity:.95}

/* platform */
.platform{left:60px;top:1500px;width:690px;height:390px;background:var(--ice);border-radius:20px;padding:28px 30px}
.platform-eyebrow{font-family:"Nunito",sans-serif;font-weight:900;font-size:17px}
.platform-title{font-family:"Nunito",sans-serif;font-weight:900;font-size:23px;color:var(--blue);margin:6px 0 10px;white-space:nowrap}
.platform-body{font-size:18px;line-height:1.32;font-weight:500}
.pillars{left:780px;top:1500px;width:360px;display:flex;flex-direction:column;gap:18px}
.pillar{height:72px;display:flex;align-items:center;justify-content:center;font-family:"Nunito",sans-serif;font-weight:800;font-size:24px}
.pillar.light{background:var(--ice);color:var(--blue)}
.pillar.dark{background:var(--navy);color:var(--white)}

/* features */
.features{left:60px;top:1935px;width:1080px;height:110px;display:flex;align-items:center}
.feature{flex:1;display:flex;align-items:center;gap:14px;padding:0 14px;border-right:3px solid var(--navy);height:90px}
.feature:last-child{border-right:none}
.feature-icon{width:72px;height:72px;flex:none;border-radius:50%;background:var(--navy);display:flex;align-items:center;justify-content:center}
.feature-label{font-family:"Nunito",sans-serif;font-weight:800;font-size:19px;line-height:1.2;white-space:nowrap}

/* footer */
.footer{left:0;top:2140px;width:1200px;height:110px}
.footer-tag{left:82px;top:2176px;color:var(--white);font-family:"Nunito",sans-serif;font-weight:800;font-size:28px}
.footer-url{left:610px;top:2172px;display:flex;align-items:center;gap:14px;color:var(--white);font-family:"Nunito",sans-serif;font-weight:900;font-size:32px;white-space:nowrap}
</style>
</head>
<body>
<main class="sheet">

  <!-- hero -->
  <svg class="abs hero-photo" viewBox="0 0 1200 720" role="img" aria-label="Photograph of a business professional holding a tablet projecting holographic financial charts and dashboards">
    <defs>
      <linearGradient id="photoTone" x1="0" y1="0" x2="1" y2="1">
        <stop offset="0" stop-color="#c9ccd2"/>
        <stop offset=".35" stop-color="#d99b72"/>
        <stop offset=".65" stop-color="#5b6472"/>
        <stop offset="1" stop-color="#1c2028"/>
      </linearGradient>
    </defs>
    <polygon points="590,0 1200,0 1200,720 720,720" fill="url(#photoTone)"/>
  </svg>
  <svg class="abs hero-panel" viewBox="0 0 1200 720" aria-hidden="true">
    <defs>
      <linearGradient id="panelTone" x1="0" y1="0" x2="1" y2="1">
        <stop offset="0" stop-color="#1f5aa6"/>
        <stop offset="1" stop-color="#17386b"/>
      </linearGradient>
    </defs>
    <polygon points="0,170 635,170 702,720 0,720" fill="url(#panelTone)"/>
  </svg>

  <div class="abs brand">
    <div class="brand-mark"></div>
    <div>
      <div class="brand-name">HARBORLINE PORTFOLIO<br>PARTNERS</div>
      <div class="brand-tag">Where Infrastructure Meets Insight</div>
    </div>
  </div>

  <section class="abs hero-copy">
    <h1 class="hero-title">Master Servicing &amp;<br>Portfolio Optimization</h1>
    <p class="hero-sub">End-to-End Post Default Management Strategy,<br>Recovery &amp; Compliance</p>
    <div class="hero-rule"></div>
    <p class="hero-body">HPP delivers master servicing solutions powered by proprietary technology and automation. We centralize back-office operations, optimize recovery performance, and embed compliance controls across the full post-default lifecycle, reducing client overhead while increasing transparency and results.</p>
  </section>

  <!-- services -->
  <div class="abs service-band"></div>
  <section class="abs services">
    <div class="service">
      <div class="service-head">
        <div class="service-icon"><svg width="28" height="28" viewBox="0 0 30 30"><rect x="3" y="18" width="4" height="8" fill="#fff"/><rect x="10" y="14" width="4" height="12" fill="#fff"/><rect x="17" y="10" width="4" height="16" fill="#fff"/><rect x="24" y="5" width="4" height="21" fill="#fff"/><path d="M3 13 L12 7 L18 9 L27 2" stroke="#fff" stroke-width="2" fill="none"/></svg></div>
        <h2 class="service-title">Strategy &amp; Recovery<br>Optimization</h2>
      </div>
      <ul>
        <li>Recovery &amp; Liquidation Optimization</li>
        <li>Settlement Campaigns</li>
        <li>Payer Base Development &amp; Retention</li>
        <li>Penetration &amp; Conversion Tracking</li>
        <li>Omni-Channel &amp; Champion Challenger Collection Strategy</li>
      </ul>
    </div>
    <div class="service">
      <div class="service-head">
        <div class="service-icon"><svg width="28" height="28" viewBox="0 0 30 30"><rect x="5" y="2" width="17" height="23" rx="2" fill="none" stroke="#fff" stroke-width="2.4"/><path d="M9 8h9M9 12h9M9 16h5" stroke="#fff" stroke-width="2"/><circle cx="22" cy="22" r="6" fill="#fff"/><path d="M19 22l2 2 4-4" stroke="#1f5aa6" stroke-width="2" fill="none"/></svg></div>
        <h2 class="service-title">Compliance &amp; Risk<br>Oversight</h2>
      </div>
      <ul>
        <li>Collection Agency Oversight</li>
        <li>Regulatory Compliance Audits (FDCPA, FCRA, UDAAP)</li>
        <li>SOL Calculation &amp; Tracking</li>
        <li>Reg F Balance Reconciliations Bankruptcy, Military &amp; Deceased Checks</li>
        <li>Complaint Management &amp; Monitoring</li>
      </ul>
    </div>
    <div class="service">
      <div class="service-head">
        <div class="service-icon"><svg width="28" height="28" viewBox="0 0 30 30"><circle cx="15" cy="15" r="12" fill="none" stroke="#fff" stroke-width="2.4" stroke-dasharray="5 3"/><circle cx="15" cy="12" r="4" fill="#fff"/><path d="M8 23c1-4 4-6 7-6s6 2 7 6" fill="#fff"/></svg></div>
        <h2 class="service-title">Operations &amp; Portfolio<br>Management</h2>
      </div>
      <ul>
        <li>Rigorous Placement &amp; Recall Processing</li>
        <li>Daily Balance Calculations &amp; Data Management Bank &amp; Inventory Reconciliation</li>
        <li>Portfolio Database Access Executive Reporting</li>
        <li>Bankruptcy Monitoring &amp; Support</li>
      </ul>
    </div>
  </section>

  <!-- performance -->
  <h2 class="abs snapshot-title">PERFORMANCE SNAPSHOT</h2>
  <section class="abs stats">
    <div class="stat"><div class="stat-num">$155+ <small>Million</small></div><div class="stat-label">Portfolio Collections<br>Administered</div></div>
    <div class="stat"><div class="stat-num">573,000+</div><div class="stat-label">Defaulted Accounts<br>Managed</div></div>
    <div class="stat"><div class="stat-num">3,700+</div><div class="stat-label">Compliance Audits<br>Conducted</div></div>
    <div class="stat"><div class="stat-num">21%</div><div class="stat-label">3-Year Gross<br>Collection Curve</div></div>
  </section>

  <!-- platform -->
  <section class="abs platform">
    <div class="platform-eyebrow">LedgerIQ™</div>
    <h2 class="platform-title">The Intelligence Behind Every Compliant Command.</h2>
    <p class="platform-body">LedgerIQ is HPP's compliance-led portfolio command intelligence platform — where regulatory authority and operational execution are unified under a single, AI-powered command center. Its live dashboard gives institutional clients total command over the post-default lifecycle: real-time compliance audit status across 15+ regulatory frameworks, centralized asset inventory with account-level drill-down, and automated workflow execution for placements, recalls, reconciliations, and recovery campaigns. LedgerIQ doesn't just display intelligence — it commands with it.</p>
  </section>
  <section class="abs pillars">
    <div class="pillar light">Optimized Recoveries</div>
    <div class="pillar dark">Proven Scale</div>
    <div class="pillar light">Embedded Compliance</div>
    <div class="pillar dark">Measurable Outcomes</div>
  </section>

  <!-- features -->
  <section class="abs features">
    <div class="feature">
      <div class="feature-icon"><svg width="40" height="40" viewBox="0 0 30 30"><rect x="5" y="2" width="17" height="23" rx="2" fill="none" stroke="#fff" stroke-width="2.2"/><path d="M9 8h9M9 12h9M9 16h5" stroke="#fff" stroke-width="2"/><circle cx="22" cy="22" r="6" fill="#fff"/><path d="M19 22l2 2 4-4" stroke="#1b3a6e" stroke-width="2" fill="none"/></svg></div>
      <div class="feature-label">Built-In Compliance<br>Controls</div>
    </div>
    <div class="feature">
      <div class="feature-icon"><svg width="42" height="42" viewBox="0 0 30 30"><g stroke="#fff" stroke-width="1.8"><path d="M15 15L15 4M15 15L25 10M15 15L24 23M15 15L6 23M15 15L5 10"/></g><circle cx="15" cy="15" r="4" fill="#fff"/><g fill="#fff"><circle cx="15" cy="4" r="2.6"/><circle cx="25" cy="10" r="2.6"/><circle cx="24" cy="23" r="2.6"/><circle cx="6" cy="23" r="2.6"/><circle cx="5" cy="10" r="2.6"/></g></svg></div>
      <div class="feature-label">Centralized Asset<br>Visibility</div>
    </div>
    <div class="feature">
      <div class="feature-icon"><svg width="42" height="42" viewBox="0 0 30 30"><circle cx="15" cy="15" r="11" fill="none" stroke="#fff" stroke-width="2" stroke-dasharray="14 4"/><circle cx="15" cy="15" r="6" fill="none" stroke="#fff" stroke-width="2.2"/><circle cx="15" cy="15" r="2.2" fill="#fff"/></svg></div>
      <div class="feature-label">Automated Workflow &amp;<br>Recovery Execution</div>
    </div>
  </section>

  <!-- footer -->
  <svg class="abs footer" viewBox="0 0 1200 110" aria-hidden="true">
    <defs>
      <linearGradient id="urlTone" x1="0" y1="0" x2="1" y2="0">
        <stop offset="0" stop-color="#2a6fc4"/>
        <stop offset="1" stop-color="#1b3a6e"/>
      </linearGradient>
    </defs>
    <rect width="1200" height="110" fill="#1b3a6e"/>
    <polygon points="500,0 1200,0 1200,110 478,110" fill="#ffffff"/>
    <polygon points="512,0 1200,0 1200,110 490,110" fill="url(#urlTone)"/>
  </svg>
  <p class="abs footer-tag">Your Trusted Advisor.</p>
  <p class="abs footer-url">
    <svg width="34" height="34" viewBox="0 0 30 30"><circle cx="15" cy="15" r="14" fill="#fff"/><g fill="none" stroke="#1f5aa6" stroke-width="1.6"><circle cx="15" cy="15" r="9"/><ellipse cx="15" cy="15" rx="4" ry="9"/><path d="M6 15h18M8 10h14M8 20h14"/></g></svg>
    www.harborlineportfolio.com
  </p>
</main>
</body>
</html>
```